Business Book - Building Calm Habits at the Office (Less Noise, More Focus Each Day)

I'm looking for a cover that appeals to successful business people who are used to reading business titles.

The cover should feel familiar and fit in with the existing canon of bestselling business books with a vibrant, but professional look (see attached).

I want my book to stand out, but not to be frivolous. Abstract is probably best. Or close to it.

Please feel free to use my brand colours, or go with something else -

Teal
HEX #199BAB
25 / 155 / 171

Coral
HEX #EE786E
238 / 120/ 110

I don't want to include anything connected with robots or gendered assistants/business people. Or headsets.

It's only 24 hours which is mental

```html
<!DOCTYPE html>
<html lang="en">
<head>
<meta charset="utf-8">
<title>Building Calm Habits at the Office — Book Cover</title>
<link rel="stylesheet" href="https://fonts.googleapis.com/css2?family=Bebas+Neue&family=Oswald:wght@200;400&display=swap">
<style>
  :root {
    --page-bg: #e4e4e4;
    --cover-teal: #a1c4c8;
    --title-orange: #dd4d1d;
    --ink: #151515;
    --band-white: #ededed;
    --hand-navy: #2f4e8f;
  }
  * { margin: 0; padding: 0; box-sizing: border-box; }
  html, body {
    width: 1200px;
    height: 800px;
    overflow: hidden;
    background: var(--page-bg);
  }
  .cover {
    position: absolute;
    left: 358px;
    top: 30px;
    width: 484px;
    height: 740px;
    background: var(--cover-teal);
    overflow: hidden;
  }
  .title {
    position: absolute;
    left: 92px;
    top: 42px;
    width: 310px;
    display: flex;
    flex-direction: column;
    align-items: center;
    font-family: "Bebas Neue", "Oswald", sans-serif;
    font-weight: 400;
    color: var(--title-orange);
    line-height: 0.8;
  }
  .title-line { display: block; white-space: nowrap; }
  .title-line--medium { font-size: 78px; }
  .title-line--huge { font-size: 140px; }
  .title-line--small { font-size: 54px; }
  .title-line--large { font-size: 104px; }
  .accent-dot {
    position: absolute;
    left: 236px;
    top: 379px;
    width: 62px;
    height: 62px;
    border-radius: 50%;
    background: var(--title-orange);
  }
  .subtitle {
    position: absolute;
    z-index: 2;
    left: 0;
    top: 376px;
    width: 100%;
    text-align: center;
    font-family: "Oswald", sans-serif;
    font-weight: 400;
    font-size: 19px;
    line-height: 1.2;
    letter-spacing: -0.2px;
    color: var(--ink);
    text-transform: uppercase;
  }
  .hand-illustration {
    position: absolute;
    left: 137px;
    top: 415px;
    width: 200px;
    height: 251px;
  }
  .author-band {
    position: absolute;
    left: 0;
    top: 666px;
    width: 100%;
    height: 74px;
    background: var(--band-white);
    display: flex;
    align-items: center;
    justify-content: center;
  }
  .author-name {
    font-family: "Oswald", sans-serif;
    font-weight: 200;
    font-size: 28px;
    letter-spacing: 0.55em;
    margin-right: -0.55em;
    color: var(--ink);
  }
</style>
</head>
<body>
  <main class="cover">
    <h1 class="title">
      <span class="title-line title-line--medium">Building</span>
      <span class="title-line title-line--huge">Calm</span>
      <span class="title-line title-line--small">Habits at the</span>
      <span class="title-line title-line--large">Office</span>
    </h1>

    <div class="accent-dot"></div>
    <p class="subtitle">Less Noise, More Focus Each Day</p>

    <svg class="hand-illustration" role="img" aria-label="Stippled blue illustration of a hand reaching up, fingertip touching the orange dot" viewBox="0 0 200 251" preserveAspectRatio="none">
      <defs>
        <linearGradient id="handTone" x1="0" y1="0" x2="0" y2="1">
          <stop offset="0" stop-color="#2f4e8f" stop-opacity="0.15"/>
          <stop offset="0.5" stop-color="#2f4e8f" stop-opacity="0.45"/>
          <stop offset="1" stop-color="#2f4e8f" stop-opacity="0.7"/>
        </linearGradient>
      </defs>
      <rect x="0" y="0" width="200" height="251" fill="url(#handTone)"/>
    </svg>

    <footer class="author-band">
      <p class="author-name">AUTHOR NAME</p>
    </footer>
  </main>
</body>
</html>
```